Business card for our large format printing and installation business

We want a professional looking business card for our business. We manufacture and install Signs.

On the back of the card add this info
Large Format Graphics Printing & Installations, Event Graphics, Banners, Posters, Vehicle Fleet Graphics, Boat Wraps, Wall Murals, Decals,Displays,Signs,Plaques,Digital Signs

On the Front of the card add the Tallowfern Signs logo, plus On the back of the card add the Orange Tallowfern Wraps logo. The 2 vector logos are attached to the design brief.

Target Market(s)

Local business owners

Contact Information for Business Card

Colors
f37122
f68d4e
f9ba93

Requirements
Must have
• On the Front of the card add the Tallowfern Signs logo, plus On the back of the card add the Orange Tallowfern Wraps logo. The 2 vector logos are attached to the design brief.

```html
<!DOCTYPE html>
<html lang="en">
<head>
<meta charset="utf-8">
<title>Tallowfern Signs – Business Card</title>
<link rel="stylesheet" href="https://fonts.googleapis.com/css2?family=Open+Sans:wght@400;600;700;800&display=swap">
<style>
  :root {
    --page: #ffffff;
    --frame: #9a9a9a;
    --lavender: #e2e0f1;
    --purple: #615ea8;
    --brand: #f7a12f;
    --ink-light: #ffffff;
  }
  * { margin: 0; padding: 0; box-sizing: border-box; }
  html, body { width: 1200px; height: 1200px; overflow: hidden; background: var(--page); }
  .canvas {
    position: relative;
    width: 1200px; height: 1200px;
    border: 1px solid var(--frame);
    font-family: "Open Sans", Arial, sans-serif;
  }
  .card {
    position: absolute;
    left: 261px;
    width: 678px; height: 408px;
    overflow: hidden;
  }
  .card--front { top: 163px; }
  .card--back { top: 629px; }

  .card__texture { position: absolute; inset: 0; }
  .card--front .card__texture {
    background: linear-gradient(180deg,
      var(--purple) 0%, #8a87c2 14%, var(--lavender) 30%,
      var(--lavender) 74%, #8a87c2 86%, var(--purple) 100%);
  }
  .card--back .card__texture {
    background: linear-gradient(90deg,
      var(--lavender) 0%, var(--lavender) 36%, #9a97cc 46%,
      var(--purple) 58%, var(--purple) 100%);
  }

  .wordmark {
    position: absolute;
    color: var(--brand);
    font-weight: 800;
    line-height: 1;
    white-space: nowrap;
  }
  .wordmark__main { display: block; }
  .wordmark__sub { display: block; text-align: right; }

  .card--front .wordmark { left: 88px; top: 150px; width: 500px; }
  .card--front .wordmark__main { font-size: 82px; letter-spacing: -1px; }
  .card--front .wordmark__sub { font-size: 68px; margin-top: -4px; }

  .card--back .wordmark {
    left: 112px; top: 205px;
    width: 345px;
    transform: translate(-50%, -50%) rotate(-90deg);
  }
  .card--back .wordmark__main { font-size: 57px; letter-spacing: -1px; }
  .card--back .wordmark__sub { font-size: 44px; margin-top: -2px; }

  .contact {
    position: absolute;
    left: 397px; top: 70px;
    color: var(--ink-light);
  }
  .contact__name { font-size: 27px; font-weight: 600; line-height: 1.1; }
  .contact__title { font-size: 18px; font-weight: 700; line-height: 1.2; margin-bottom: 52px; }
  .contact__list { list-style: none; }
  .contact__item {
    display: flex; align-items: flex-start;
    font-size: 17px; line-height: 22px;
    margin-bottom: 15px;
  }
  .contact__item--email { margin-bottom: 28px; }
  .contact__item:last-child { margin-bottom: 0; }
  .contact__icon { width: 14px; height: 14px; margin: 4px 12px 0 3px; flex: none; }
</style>
</head>
<body>
<main class="canvas">

  <section class="card card--front" aria-label="Card front">
    <div class="card__texture" role="img" aria-label="Purple and lavender splash texture with flying silhouettes"></div>
    <div class="wordmark">
      <span class="wordmark__main">Tallowfern</span>
      <span class="wordmark__sub">Signs</span>
    </div>
  </section>

  <section class="card card--back" aria-label="Card back">
    <div class="card__texture" role="img" aria-label="Lavender to purple splash texture with flying silhouettes"></div>
    <div class="wordmark">
      <span class="wordmark__main">Tallowfern</span>
      <span class="wordmark__sub">Signs</span>
    </div>

    <div class="contact">
      <p class="contact__name">Marcus Ellery</p>
      <p class="contact__title">CEO</p>
      <ul class="contact__list">
        <li class="contact__item contact__item--email">
          <svg class="contact__icon" viewBox="0 0 14 14" fill="none" stroke="#fff" stroke-width="1.1"><rect x="1" y="3" width="12" height="8.5" rx="1"/><path d="M1 3.5l6 4.5 6-4.5"/></svg>
          <span>marcus@tallowfern.net</span>
        </li>
        <li class="contact__item">
          <svg class="contact__icon" viewBox="0 0 14 14" fill="none" stroke="#fff" stroke-width="1.1"><circle cx="7" cy="7" r="6.2"/><path d="M7 11s-2.8-3-2.8-5a2.8 2.8 0 0 1 5.6 0c0 2-2.8 5-2.8 5z"/><circle cx="7" cy="6" r="0.9"/></svg>
          <span>1840 Harbor Crest Lane #7<br>Seabright Shores, FL 33120</span>
        </li>
        <li class="contact__item">
          <svg class="contact__icon" viewBox="0 0 14 14" fill="none" stroke="#fff" stroke-width="1.1"><circle cx="7" cy="7" r="6.2"/><path d="M5 3.5c-.8.6-1 1.6-.5 2.8.6 1.5 1.7 2.8 3 3.6.9.5 1.7.4 2.3-.2l-1.2-1.3-.9.5c-.8-.5-1.5-1.3-1.9-2.2l.7-.7L5.8 4z"/></svg>
          <span>Office: 954-555-0148<br>Direct: 786-555-0172</span>
        </li>
        <li class="contact__item">
          <svg class="contact__icon" viewBox="0 0 14 14" fill="none" stroke="#fff" stroke-width="1.1"><circle cx="7" cy="7" r="6.2"/><ellipse cx="7" cy="7" rx="2.6" ry="6.2"/><path d="M0.8 7h12.4M1.8 4h10.4M1.8 10h10.4"/></svg>
          <span>www.Tallowfernwraps.com</span>
        </li>
      </ul>
    </div>
  </section>

</main>
</body>
</html>
```